International Dating Site for modern people

We need a site design for a brand new dating site. Feel free to express your ideas and creativity. The final design should be creative and positive feeling, warm.

major elements:
- main page
- login/logout (form)
- profile editing (form)
- profile page with pictures
- search page and results page (form, table)
- a message box or the header in the main page with the following theme, feeling:
winter, spring, summer, autumn, christmas, easter, new year
- blog subpage (title, content)
- menu (login/blog/search/profile/logout)
- footer (impressum, faq, contact, privacy policy)

Target Market(s)

people between 21 and 45

Industry/Entity Type

Social

Number of Pages Required

4 page

Font styles to use
Sans Serif

Requirements
Must have
• happy, positive, warm look and feel and responsive design (plan to target different devices, the final and coded version will be responsive but please think of it when you design elements)
Nice to have
• creative

```html
<!DOCTYPE html>
<html lang="en">
<head>
<meta charset="utf-8">
<title>International Dating Site</title>
<link href="https://fonts.googleapis.com/css2?family=Raleway:wght@300;400;500;600;700&family=Open+Sans:wght@400;600;700&display=swap" rel="stylesheet">
<style>
:root{
  --pink:#fd4e5d;
  --pink-dark:#e73a4a;
  --ink:#141414;
  --text:#2b2b2b;
  --muted:#555;
  --white:#fff;
  --grey-bg:#e9e9e9;
  --black:#000;
  --line:#cfcfcf;
}
*{box-sizing:border-box;margin:0;padding:0}
html,body{width:1200px;height:2889px;overflow:hidden;background:var(--white)}
body{font-family:"Open Sans",Arial,sans-serif;color:var(--text);position:relative}
.page{position:relative;width:1200px;height:2889px;overflow:hidden}
.abs{position:absolute}
.btn-outline{position:absolute;display:flex;align-items:center;justify-content:center;font-family:"Open Sans",sans-serif;font-size:15px;border:2px solid var(--pink);color:var(--ink);background:var(--white)}

/* top bar */
.topbar{left:0;top:0;width:1200px;height:35px;background:var(--black)}
.social-top{left:58px;top:8px;display:flex;gap:8px}
.social-top span{width:19px;height:19px;border:1.5px solid #ddd;border-radius:50%;display:block}
.account{right:30px;top:0;height:35px;display:flex;align-items:center;gap:14px;color:#eee;font-size:14px}
.account .sep{color:#999}

/* hero */
.hero{left:0;top:35px;width:1200px;height:604px;background:radial-gradient(ellipse at 70% 30%,#d9a46a 0%,#8a5a3a 40%,#3d2418 80%,#2a1810 100%)}
.header{left:0;top:35px;width:1200px;height:109px;background:rgba(230,225,220,.78)}
.logo{left:58px;top:52px;font-family:"Raleway",sans-serif;font-weight:700;color:var(--ink);line-height:1}
.logo .l1{display:block;font-size:40px}
.logo .l2{display:block;font-size:24px;margin-top:4px}
.nav{top:76px;left:0;font-family:"Raleway",sans-serif;font-size:20px;color:var(--ink)}
.nav a{position:absolute;color:inherit;text-decoration:none;white-space:nowrap}
.hero-title{left:0;width:1200px;top:378px;text-align:center;font-family:"Raleway",sans-serif;font-weight:400;font-size:57px;line-height:68px;color:var(--white)}
.hero-btn{left:519px;top:528px;width:162px;height:50px;border:2px solid var(--white);color:var(--white);background:transparent}

/* feature cards */
.card{top:614px;width:237px;height:295px;background:var(--pink);border:3px solid var(--white);box-shadow:0 2px 6px rgba(0,0,0,.25);display:flex;flex-direction:column;align-items:center}
.card svg{margin-top:40px}
.card p{position:absolute;top:198px;width:100%;text-align:center;font-family:"Raleway",sans-serif;font-size:27px;color:var(--white)}

/* welcome */
.welcome-title{left:0;width:1200px;top:952px;text-align:center;font-family:"Raleway",sans-serif;font-weight:600;font-size:46px;color:var(--ink)}
.welcome-title em{font-style:normal;color:var(--pink)}
.welcome-text{left:235px;width:730px;top:1030px;text-align:center;font-size:14.5px;line-height:28px;color:var(--muted)}
.welcome-btn{left:519px;top:1138px;width:162px;height:47px}

/* gallery */
.photo{top:1235px;width:227px;height:215px}

/* search */
.search-band{left:0;top:1502px;width:1200px;height:491px;background:radial-gradient(ellipse at 60% 45%,#4a4a44 0%,#2a2b27 45%,#151613 100%)}
.search-box{left:60px;top:1591px;width:360px;height:352px;background:var(--pink);color:var(--white)}
.search-box h3{margin-top:30px;text-align:center;font-size:16px;font-weight:700;line-height:26px}
.field{position:absolute;left:0;display:flex;align-items:center;font-size:13px}
.field label{width:133px;text-align:right;padding-right:18px}
.select{height:29px;background:var(--white);color:var(--ink);font-size:13px;display:flex;align-items:center;justify-content:space-between;padding:0 8px}
.select::after{content:"";border:5px solid transparent;border-top:6px solid var(--ink);margin-top:5px}
.search-btn{position:absolute;left:151px;top:278px;width:110px;height:36px;background:var(--white);color:var(--ink);font-size:13px;display:flex;align-items:center;justify-content:center;gap:8px}

/* posts */
.posts-title{left:0;width:1200px;top:2025px;text-align:center;font-family:"Raleway",sans-serif;font-size:50px;color:var(--ink)}
.posts-title em{font-style:normal;color:var(--pink)}
.post{top:2119px;width:256px}
.post .thumb{height:173px}
.post h4{margin-top:22px;font-family:"Raleway",sans-serif;font-weight:500;font-size:18px;color:var(--ink)}
.post p{margin-top:10px;font-size:13px;line-height:22px;color:var(--muted)}
.dots{left:0;width:1200px;top:2414px;display:flex;justify-content:center;gap:9px}
.dots span{width:11px;height:11px;border-radius:50%;background:var(--black)}
.dots span.on{background:var(--pink)}

/* footer */
.footer-grey{left:482px;top:2542px;width:718px;height:309px;background:var(--grey-bg)}
.footer-photo{left:0;top:2500px;width:482px;height:351px;border:5px solid var(--ink);border-left:0;border-bottom:0;background:linear-gradient(135deg,#c9d6b8 0%,#d9b7c6 40%,#c98e7a 70%,#7a5a4a 100%)}
.footer h5{font-family:"Raleway",sans-serif;font-weight:700;font-size:17px;color:var(--ink);letter-spacing:.3px}
.info{left:557px;top:2620px;width:300px}
.info-row{display:flex;gap:16px;font-size:13px;line-height:22px;color:var(--text);margin-top:22px}
.info-row svg{flex:none;margin-top:3px}
.info-social{display:flex;gap:16px;margin:20px 0 0 32px}
.info-social span{width:11px;height:11px;border-radius:50%;background:#8a8a8a}
.faq{left:884px;top:2620px;width:235px}
.input{height:35px;border:1.5px solid #bbb;background:var(--white);font-size:11px;color:var(--ink);padding:0 10px;display:flex;align-items:center;margin-top:7px}
.input:first-of-type{margin-top:22px}
.submit{margin-top:20px;width:100px;height:33px;background:var(--black);color:var(--white);font-size:12px;font-weight:700;display:flex;align-items:center;justify-content:center}
.bottombar{left:0;top:2851px;width:1200px;height:38px;background:var(--black);color:var(--white);font-size:11px;display:flex;align-items:center;justify-content:space-between;padding:0 58px}
.bottombar .links{display:flex;gap:20px}
</style>
</head>
<body>
<div class="page">

  <!-- top bar -->
  <div class="abs topbar"></div>
  <div class="abs social-top" aria-label="Social links"><span></span><span></span><span></span><span></span></div>
  <div class="abs account">
    <span>Log In</span><span class="sep">|</span><span>Logout</span>
    <svg width="14" height="14" viewBox="0 0 14 14"><circle cx="5.5" cy="5.5" r="4.3" fill="none" stroke="#fff" stroke-width="1.8"/><line x1="8.6" y1="8.6" x2="13" y2="13" stroke="#fff" stroke-width="2"/></svg>
  </div>

  <!-- hero -->
  <div class="abs hero" role="img" aria-label="Couple sharing a kiss in warm sunset light"></div>
  <div class="abs header"></div>
  <div class="abs logo"><span class="l1">International</span><span class="l2">Dating Site</span></div>
  <nav class="abs nav">
    <a style="left:688px">Home</a>
    <a style="left:793px">Blog</a>
    <a style="left:886px">Edit Profile</a>
    <a style="left:1034px">Profile page</a>
  </nav>
  <h1 class="abs hero-title">The Right Place to Meet Your<br>Soul Mate!</h1>
  <div class="btn-outline hero-btn">Read More</div>

  <!-- feature cards -->
  <div class="abs card" style="left:210px">
    <svg width="100" height="100" viewBox="0 0 100 100" fill="none" stroke="#fff" stroke-width="4" stroke-linejoin="round">
      <path d="M18 8h48v50"/><path d="M18 8v84h48V82"/>
      <line x1="28" y1="28" x2="56" y2="28"/><line x1="28" y1="40" x2="56" y2="40"/><line x1="28" y1="52" x2="50" y2="52"/><line x1="28" y1="64" x2="44" y2="64"/>
      <path d="M84 40l8 8-28 28-11 3 3-11z"/>
    </svg>
    <p>Register Now</p>
  </div>
  <div class="abs card" style="left:482px">
    <svg width="100" height="100" viewBox="0 0 100 100" fill="none" stroke="#fff" stroke-width="4">
      <circle cx="50" cy="50" r="44"/><circle cx="50" cy="38" r="15"/><path d="M22 80c5-16 16-22 28-22s23 6 28 22"/>
    </svg>
    <p>Create A Profile</p>
  </div>
  <div class="abs card" style="left:753px">
    <svg width="100" height="100" viewBox="0 0 100 100" fill="none" stroke="#fff" stroke-width="4" stroke-linejoin="round">
      <path d="M50 86C20 62 8 48 8 32 8 19 18 10 30 10c9 0 16 5 20 13 4-8 11-13 20-13 12 0 22 9 22 22 0 16-12 30-42 54z"/>
    </svg>
    <p>Find True Love</p>
  </div>

  <!-- welcome -->
  <h2 class="abs welcome-title"><em>Welcome</em> International Dating Site</h2>
  <p class="abs welcome-text">Our agency has a potential match for everyone, whether you are interested in Latin, Asian, African, Christian or senior dating. Our well-balanced gender distribution makes our service perfect for both men and women. Register on our site with a few clicks and start your partner search immediately.</p>
  <div class="btn-outline welcome-btn">Read More</div>

  <!-- gallery -->
  <div class="abs photo" style="left:8px;background:linear-gradient(180deg,#6fa8e0 0%,#a9cdf0 70%,#d9d3c4 100%)" role="img" aria-label="Two people leaping to form a heart shape against blue sky"></div>
  <div class="abs photo" style="left:247px;background:linear-gradient(135deg,#5e7a3a 0%,#b8c07a 50%,#e7d9b8 100%)" role="img" aria-label="Couple embracing among trees"></div>
  <div class="abs photo" style="left:487px;background:linear-gradient(135deg,#2f4a2a 0%,#6f8a4a 45%,#c9a583 100%)" role="img" aria-label="Couple at a dinner table outdoors"></div>
  <div class="abs photo" style="left:726px;background:linear-gradient(135deg,#3a3a3a 0%,#7a6a5a 50%,#c8b29a 100%)" role="img" aria-label="Couple kissing in the evening"></div>
  <div class="abs photo" style="left:967px;background:linear-gradient(135deg,#c9b7a5 0%,#e2d0bb 50%,#b89b7e 100%)" role="img" aria-label="Couple riding bicycles together"></div>

  <!-- search -->
  <div class="abs search-band" role="img" aria-label="Couple sitting on grass at dusk with balloons"></div>
  <div class="abs search-box">
    <h3>Serious dating with Heartline<br>Your perfect match is just a click away</h3>
    <div class="field" style="top:90px"><label>I am a</label><div class="select" style="width:175px">Man</div></div>
    <div class="field" style="top:134px"><label>Looking For a</label><div class="select" style="width:175px">Woman</div></div>
    <div class="field" style="top:178px"><label>Age</label><div class="select" style="width:68px">18</div><span style="width:39px;text-align:center">-</span><div class="select" style="width:68px">75</div></div>
    <div class="field" style="top:222px"><label>City</label><div class="select" style="width:175px;justify-content:flex-start"></div></div>
    <div class="search-btn">
      <svg width="12" height="12" viewBox="0 0 14 14"><circle cx="5.5" cy="5.5" r="4.3" fill="none" stroke="#141414" stroke-width="1.8"/><line x1="8.6" y1="8.6" x2="13" y2="13" stroke="#141414" stroke-width="2"/></svg>
      SEARCH
    </div>
  </div>

  <!-- recent posts -->
  <h2 class="abs posts-title"><em>Recent</em> posts</h2>
  <article class="abs post" style="left:60px">
    <div class="thumb" style="background:linear-gradient(135deg,#f5d27a 0%,#e39a4a 50%,#b4602e 100%)" role="img" aria-label="Couple holding hands in golden light"></div>
    <h4>Lorem ipsum dolor sit</h4>
    <p>Duis autem vel eum iriure dolor in hendrerit in vulputate velit esse moles</p>
  </article>
  <article class="abs post" style="left:335px">
    <div class="thumb" style="background:linear-gradient(135deg,#7a7a7a 0%,#c89a7e 50%,#e9d6c6 100%)" role="img" aria-label="Smiling couple cheek to cheek"></div>
    <h4>Claritas est etiam pr</h4>
    <p>Duis autem vel eum iriure dolor in hendrerit in vulputate velit esse moles</p>
  </article>
  <article class="abs post" style="left:609px">
    <div class="thumb" style="background:linear-gradient(135deg,#f4e6d6 0%,#c9a07e 45%,#6a1e22 100%)" role="img" aria-label="Two glasses of red wine in a toast"></div>
    <h4>Eodem mod</h4>
    <p>Duis autem vel eum iriure dolor in hendrerit in vulputate velit esse moles</p>
  </article>
  <article class="abs post" style="left:884px">
    <div class="thumb" style="background:linear-gradient(135deg,#3a2a22 0%,#b07a5e 50%,#e8c4a8 100%)" role="img" aria-label="Laughing couple close together"></div>
    <h4>Rem ipsum dolor</h4>
    <p>Duis autem vel eum iriure dolor in hendrerit in vulputate velit esse moles</p>
  </article>
  <div class="abs dots"><span class="on"></span><span></span><span></span><span></span><span></span></div>

  <!-- footer -->
  <footer class="footer">
    <div class="abs footer-grey"></div>
    <div class="abs footer-photo" role="img" aria-label="Couple embracing under spring blossoms"></div>
    <div class="abs info">
      <h5>STORE INFORMATION</h5>
      <div class="info-row">
        <svg width="16" height="16" viewBox="0 0 16 16" fill="none" stroke="#666" stroke-width="1.4"><path d="M2 8l6-5 6 5v6H2z"/><rect x="6.5" y="10" width="3" height="4"/></svg>
        <span>18 Maple Row, Riverside District,<br>Lakeview</span>
      </div>
      <div class="info-row">
        <svg width="16" height="16" viewBox="0 0 16 16" fill="none" stroke="#666" stroke-width="1.4"><rect x="4" y="1" width="8" height="14" rx="1.5"/><line x1="7" y1="12.5" x2="9" y2="12.5"/></svg>
        <span>+00 4455 1020</span>
      </div>
      <div class="info-row">
        <svg width="16" height="16" viewBox="0 0 16 16" fill="none" stroke="#666" stroke-width="1.4"><rect x="1.5" y="3.5" width="13" height="9"/><path d="M1.5 3.5l6.5 5 6.5-5"/></svg>
        <span>hello@heartlinemail.com</span>
      </div>
      <div class="info-social" aria-label="Social links"><span></span><span></span><span></span><span></span><span></span></div>
    </div>
    <div class="abs faq">
      <h5>FAQ</h5>
      <div class="input">Enter your Name*</div>
      <div class="input">Enter your Email*</div>
      <div class="input">Message *</div>
      <div class="submit">SUBMIT</div>
    </div>
    <div class="abs bottombar">
      <span>© 2016 Copyright International Dating Site.  All Right Reserved.</span>
      <span class="links"><span>Privacy &amp; Cookies</span><span>Terms &amp; Conditions</span></span>
    </div>
  </footer>

</div>
</body>
</html>
```